Website 950x200 Header w/ logo

I'm in need of a website header for a new site called TalesofGordo.com

The site is basically a glorified blog for myself to write my thoughts about politics, sports, TV shows, current events, whatever. I have a lot of interests.

The site is going to look very very similar to http://www.quillpostmedia.com/5930417/7-tips-for-hiring-bold-minds

but instead of having a dynamic header that becomes the picture with each article, its just going to be a static header in which I'd like to have the name of the site (Tales of Gordo) and some kind of logo, pictures, etc - I'm totally open to anything. The only thing is it needs to have a dark (probably black) background and needs to be 950x200px.

I envision a black background, with gray and white as the primary colors and then some secondary colors potentially, but again I'm open to anything as long as it's on the black background or some kind of charcoal gray or wahtever. On the site the black part will go all the way from the left of the screen to the right no matter what the window size, but I'd like to keep all the content inside of 950x200px

email me gordo.pellwick@zentramail.com if you have any questions. Thanks!

```html
<!DOCTYPE html>
<html lang="en">
<head>
<meta charset="utf-8">
<title>Tales of Gordo – 7 Tips for Hiring Bold Minds</title>
<link href="https://fonts.googleapis.com/css2?family=Antonio:wght@400;600;700&family=Oswald:wght@400;600;700&family=Roboto+Slab:wght@700&family=Lato:wght@400;700&display=swap" rel="stylesheet">
<style>
  :root {
    --backdrop: #242424;
    --header-black: #0c0c0c;
    --paper: #ffffff;
    --ink: #111111;
    --body-text: #555555;
    --muted: #8a8a8a;
    --rule: #222222;
    --accent-blue: #1aa3d9;
    --accent-green: #3fbf5a;
    --ad-coral: #f26b52;
    --sidebar-shadow: rgba(0,0,0,0.12);
  }
  * { box-sizing: border-box; margin: 0; padding: 0; }
  html, body { width: 1200px; height: 900px; overflow: hidden; background: var(--backdrop); }
  .page {
    position: absolute; left: 122px; top: 30px;
    width: 955px; height: 840px; background: var(--paper); overflow: hidden;
  }
  .site-header {
    position: absolute; left: 0; top: 0; width: 955px; height: 200px;
    background: var(--header-black);
  }
  .brand {
    position: absolute; left: 44px; top: 42px;
    display: flex; align-items: center; gap: 14px;
    font-family: "Oswald", sans-serif; font-weight: 700; color: #ffffff;
    font-size: 62px; line-height: 1; text-transform: uppercase; letter-spacing: 2px;
  }
  .brand-mark { width: 22px; height: 22px; background: #ffffff; }
  .brand-name { display: block; width: 260px; line-height: 0.98; }

  .article { position: absolute; left: 0; top: 200px; width: 605px; height: 640px; }
  .corner-band {
    position: absolute; left: 0; top: 0; width: 390px; height: 48px;
    background: linear-gradient(90deg, #e6e6e6, rgba(230,230,230,0));
  }
  .headline {
    position: absolute; left: 44px; top: 20px; width: 500px;
    font-family: "Antonio", sans-serif; font-weight: 700; font-size: 47px;
    line-height: 42px; letter-spacing: -1.6px; color: var(--ink); text-transform: uppercase;
  }
  .byline {
    position: absolute; left: 44px; top: 124px;
    font-family: "Antonio", sans-serif; font-weight: 600; font-size: 22px; letter-spacing: -0.8px;
    color: var(--accent-blue); text-transform: uppercase;
  }
  .byline span { font-family: "Roboto Slab", serif; font-weight: 700; font-size: 11px; color: var(--muted); letter-spacing: 0; margin-right: 3px; }
  .dek {
    position: absolute; left: 44px; top: 164px; width: 525px;
    font-family: "Lato", sans-serif; font-size: 13.5px; line-height: 20px; color: var(--ink);
  }
  .share-bar {
    position: absolute; left: 44px; top: 224px; width: 510px; height: 54px;
    border-top: 1px solid var(--rule); border-bottom: 1px solid var(--rule);
  }
  .share-bar svg { position: absolute; left: 0; top: 0; }
  .share-count { font-family: "Lato", sans-serif; font-weight: 700; font-size: 9px; fill: var(--ink); }
  .body-copy {
    position: absolute; left: 44px; top: 300px; width: 505px;
    font-family: "Lato", sans-serif; font-size: 15px; line-height: 23px; color: var(--body-text);
  }
  .body-copy p + p { margin-top: 12px; }
  .section-title {
    position: absolute; left: 44px; top: 568px;
    font-family: "Antonio", sans-serif; font-weight: 700; font-size: 19px; letter-spacing: -0.8px;
    color: var(--ink); text-transform: uppercase;
  }
  .body-copy.continued { top: 598px; }

  .sidebar {
    position: absolute; left: 606px; top: 200px; width: 349px; height: 640px;
    background: var(--paper); box-shadow: inset 6px 0 8px -4px var(--sidebar-shadow);
  }
  .ad { position: absolute; left: 24px; top: 22px; width: 300px; height: 249px; border: 1px solid #e4e4e4; }
  .ad-brand {
    position: absolute; left: 18px; top: 8px; font-family: "Lato", sans-serif;
    font-size: 15px; font-weight: 700; color: #222; letter-spacing: -0.3px;
  }
  .ad-collection {
    position: absolute; left: 18px; top: 28px; font-family: "Lato", sans-serif;
    font-size: 17px; line-height: 16px; color: #444; text-transform: uppercase;
  }
  .ad-photo { position: absolute; left: 6px; top: 68px; width: 130px; height: 180px;
    background: linear-gradient(180deg, #d9c7a8 0%, #b89b74 60%, #8e7456 100%); }
  .ad-offer {
    position: absolute; left: 141px; top: 0; width: 158px; height: 248px;
    background: var(--ad-coral); color: #fff; text-align: center; font-family: "Lato", sans-serif;
    padding-top: 66px;
  }
  .ad-offer .big { font-family: "Oswald", sans-serif; font-size: 26px; line-height: 26px; }
  .ad-offer .small { font-size: 10px; line-height: 12px; }
  .ad-offer .mid { font-family: "Oswald", sans-serif; font-weight: 600; font-size: 17px; line-height: 18px; letter-spacing: 0.5px; }
  .ad-offer .cta { font-size: 14px; margin-top: 14px; }
  .ad-offer .cta u { text-underline-offset: 2px; }
  .ad-label {
    position: absolute; left: 24px; top: 273px; width: 300px; text-align: center;
    font-family: "Lato", sans-serif; font-size: 9px; color: #aaa; letter-spacing: 0.3px;
  }
  .section-name {
    position: absolute; left: 24px; top: 312px;
    font-family: "Antonio", sans-serif; font-weight: 700; font-size: 23px; letter-spacing: -0.6px; color: var(--ink);
  }
  .section-tagline {
    position: absolute; left: 24px; top: 344px;
    font-family: "Roboto Slab", serif; font-weight: 700; font-size: 11px; color: var(--muted); text-transform: uppercase;
  }
  .side-rule { position: absolute; left: 24px; width: 300px; height: 1px; background: var(--rule); }
  .editor-label {
    position: absolute; left: 24px; top: 408px;
    font-family: "Roboto Slab", serif; font-weight: 700; font-size: 13px; color: var(--ink); text-transform: uppercase;
  }
  .editor-name {
    position: absolute; left: 24px; top: 426px;
    font-family: "Antonio", sans-serif; font-size: 22px; letter-spacing: -0.8px; color: var(--muted); text-transform: uppercase;
  }
  .issue-date {
    position: absolute; left: 24px; top: 479px; width: 300px; height: 54px;
    background: #000; display: flex; align-items: center; padding-left: 12px; gap: 12px;
  }
  .issue-date .num { font-family: "Antonio", sans-serif; font-size: 38px; color: #fff; letter-spacing: -1px; }
  .issue-date .words {
    font-family: "Oswald", sans-serif; font-weight: 600; font-size: 13px; line-height: 17px;
    color: var(--accent-green); text-transform: uppercase; letter-spacing: 0.3px;
  }
  .picks-label {
    position: absolute; left: 24px; top: 578px;
    font-family: "Roboto Slab", serif; font-weight: 700; font-size: 13px; color: var(--ink); text-transform: uppercase; letter-spacing: 0.3px;
  }
  .pick-photo { position: absolute; top: 599px; height: 50px; }
  .pick-one { left: 24px; width: 148px; background: linear-gradient(135deg, #6b4a2a, #b78b54 50%, #4d3420); }
  .pick-two { left: 174px; width: 150px; background: linear-gradient(135deg, #5a3b24, #9c7246 50%, #3c2818); }
</style>
</head>
<body>
<main class="page">
  <header class="site-header">
    <div class="brand">
      <span class="brand-mark"></span>
      <span class="brand-name">Tales of Gordo</span>
    </div>
  </header>

  <article class="article">
    <div class="corner-band"></div>
    <h1 class="headline">8 Ways to Win the Race for Creative Talent</h1>
    <p class="byline"><span>BY:</span>Marcus Venn</p>
    <p class="dek">The Brightwell’s Marcus Venn talks about what, beyond a paycheck, companies can offer to attract and motivate creative talent.</p>

    <div class="share-bar">
      <svg width="510" height="54" viewBox="0 0 510 54">
        <g transform="translate(13,26)">
          <circle r="9" fill="none" stroke="#111" stroke-width="2.4"/>
          <path d="M-7,5 L-9,10 L-3,8" fill="#111"/>
        </g>
        <g transform="translate(52,26)">
          <circle r="10" fill="#111"/>
          <path d="M-5,0 H5 M0,-5 V5" stroke="#fff" stroke-width="2.4"/>
        </g>
        <circle cx="91" cy="26" r="10" fill="#111"/>
        <circle cx="131" cy="26" r="10" fill="#111"/>
        <circle cx="171" cy="26" r="10" fill="#111"/>
        <text class="share-count" x="178" y="14">255</text>
        <circle cx="212" cy="26" r="10" fill="#111"/>
        <text class="share-count" x="218" y="14">127</text>
      </svg>
    </div>

    <div class="body-copy">
      <p>Many creative businesses limit their talent recruitment and retention strategies to money and flattery.</p>
      <p>But companies adept at unlocking what I describe as Profitable Creativity are built on more sustainable practices. Many of these, I learned first hand over a decade building a company filled with demanding, world-class talent. In that time, we lost not one of our artists to a competitor. The others I’ve experienced in my work as a confidant to some of the world’s most successful chief creative officers and company owners. In all, there are eight practices. And seven come with the added benefit that they cost nothing to implement.</p>
    </div>
    <h2 class="section-title">1. Build an Evangelical Business</h2>
    <div class="body-copy continued">
      <p>Creative people yearn to make one thing more than any other. A difference. They want to solve problems they believe are important. Ten</p>
    </div>
  </article>

  <aside class="sidebar">
    <div class="ad">
      <p class="ad-brand">MAISON LUNE</p>
      <p class="ad-collection">2013 Spring<br>Collection</p>
      <div class="ad-photo" role="img" aria-label="Model wearing a beige trench coat"></div>
      <div class="ad-offer">
        <p class="big">£15 OFF*</p>
        <p class="small">YOUR FIRST ORDER</p>
        <p class="mid">+<br>FREE DELIVERY</p>
        <p class="small">USE CODE 4708</p>
        <p class="cta">&gt;&gt; <u>SHOP NOW</u></p>
      </div>
    </div>
    <p class="ad-label">ADVERTISEMENT</p>

    <h3 class="section-name">Idea.FORGE</h3>
    <p class="section-tagline">Creativity \ Culture \ Commerce</p>
    <div class="side-rule" style="top:391px"></div>
    <p class="editor-label">Editor:</p>
    <p class="editor-name">Dana Holloway</p>

    <div class="issue-date">
      <span class="num">03 / 14</span>
      <span class="words">Two thousand and<br>thirteen</span>
    </div>

    <div class="side-rule" style="top:569px"></div>
    <p class="picks-label">Editor’s Picks</p>
    <div class="pick-photo pick-one" role="img" aria-label="Warmly lit interior scene"></div>
    <div class="pick-photo pick-two" role="img" aria-label="Group of people in a wood-panelled room"></div>
  </aside>
</main>
</body>
</html>
```